Graphic Design For Website Banner + 4 Product Images - More Work To Follow

We are in the process of launching a new website. I need to design a banner for the homepage, as well as some graphics for my product images.

Please find attached -

1) My current logo.
2) Banner Sample + Product Image Sample - both of these are a screenshot from a common website that I like the design and style of.
3) Colour Scheme Sample 1 - saved image showing colour scheme for Brushwillow that I like.
4) Colour Scheme Sample 2 - Saved image showing colour scheme for Tarlo that I like.
5) Sample 1-4 - These are colour palette samples I created online showing what I like.
6) 4 blank product images to show what is required in the design.

To summarise I'll like to create a banner design and product images similar to what's been attached and have a consistent colour theme throughout. I'm happy to adjust the colours in my logo to match the final designs.

To begin with I'll be requesting 1 banner design and 4 product images. I'll have more work for the successful designer.

Banner -
Size to be 950x300. To contain the following wording -
Quality Printing
Offset|Digital|Wideformat
Deal Direct & Save
Possibly include some product images like the sample banner attached.

Product Images -
Size to be 263x263
1) Business Cards
2) Folded Brochures
3) Flyers
4) Presentation Folders
I've attached blank sample images of all 4 for your reference.

Please feel free to ask any questions as I'm happy to give further direction.

Target Market(s)

We are a commercial Printer offering a range of printed products

Font styles to use
Serif
Sans Serif

Colors
34a6d7
33b8a4
3277b5
86cfc7
86cae7
85acd3
00a990
0393ce
0255a3

```html
<!DOCTYPE html>
<html lang="en">
<head>
<meta charset="utf-8">
<title>Harbor Press Co – Business Cards</title>
<link rel="stylesheet" href="https://fonts.googleapis.com/css2?family=Quicksand:wght@300;400;700&display=swap">
<style>
  :root {
    --white: #ffffff;
    --panel-teal: #dff0ef;
    --brand-blue: #0393ce;
    --mint: #8fd3c9;
    --grey-text: #7d7d80;
    --rule-grey: #c4c8ca;
    --card-top: #ffffff;
    --card-bottom: #e3f2f1;
  }
  * { margin: 0; padding: 0; box-sizing: border-box; }
  html, body { width: 1200px; height: 1200px; overflow: hidden; background: var(--white); }
  body { font-family: "Quicksand", sans-serif; }
  .canvas { position: relative; width: 1200px; height: 1200px; }

  .panel { position: absolute; left: 57px; top: 57px; width: 1082px; height: 1082px; background: var(--panel-teal); }
  .corner { position: absolute; left: 0; top: 0; width: 455px; height: 483px; background: var(--white); }

  .brand { display: flex; align-items: center; gap: 14px; font-family: "Quicksand", sans-serif; font-weight: 700; color: var(--brand-blue); line-height: 1; white-space: nowrap; }
  .brand .mark { background: var(--brand-blue); flex: none; }

  .header-brand { position: absolute; left: 58px; top: 140px; font-size: 44px; }
  .header-brand .mark { width: 30px; height: 30px; }

  .product-title { position: absolute; left: 58px; top: 325px; font-weight: 300; font-size: 39px; line-height: 55px; letter-spacing: 2px; color: var(--mint); }

  .card { position: absolute; width: 465px; height: 302px; background: linear-gradient(135deg, var(--card-top) 35%, var(--card-bottom) 100%); box-shadow: 4px 8px 14px rgba(60, 90, 95, 0.28); }
  .card-back { left: 569px; top: 382px; display: flex; align-items: center; justify-content: center; }
  .card-back .brand { font-size: 30px; gap: 10px; }
  .card-back .mark { width: 20px; height: 20px; }

  .card-front { left: 160px; top: 598px; }
  .card-front .brand { position: absolute; left: 20px; top: 30px; font-size: 24px; gap: 8px; }
  .card-front .mark { width: 16px; height: 16px; }

  .contact { position: absolute; left: 240px; top: 140px; width: 204px; color: var(--grey-text); }
  .contact .name { font-weight: 300; font-size: 22px; letter-spacing: 4px; line-height: 26px; }
  .contact .role { font-weight: 400; font-size: 17px; letter-spacing: 2px; line-height: 22px; }
  .contact .rule { height: 2px; background: var(--rule-grey); margin: 6px 0 8px; }
  .contact ul { list-style: none; }
  .contact li { display: flex; align-items: center; gap: 12px; font-size: 13.5px; height: 26.5px; }
  .contact svg { width: 16px; height: 16px; fill: var(--grey-text); flex: none; }
</style>
</head>
<body>
<main class="canvas">
  <div class="panel"></div>
  <div class="corner"></div>

  <div class="brand header-brand"><span class="mark"></span>Harbor Press Co</div>
  <h1 class="product-title">Business<br>Cards</h1>

  <section class="card card-back">
    <div class="brand"><span class="mark"></span>Harbor Press Co</div>
  </section>

  <section class="card card-front">
    <div class="brand"><span class="mark"></span>Harbor Press Co</div>
    <div class="contact">
      <p class="name">NAME</p>
      <p class="role">Title</p>
      <div class="rule"></div>
      <ul>
        <li><svg viewBox="0 0 16 16"><path d="M1 3h14v10H1z M2.5 4.5 8 9l5.5-4.5v-.3H2.5z" fill-rule="evenodd"/></svg>email address</li>
        <li><svg viewBox="0 0 16 16"><path d="M4 1.5 6.3 4 5 6c.8 1.9 2.5 3.6 4.5 4.5l2-1.3 2.5 2.3-1.6 2.2C7.5 13.5 2.5 8.5 2 3.2z"/></svg>phone</li>
        <li><svg viewBox="0 0 16 16"><path d="M8 1a5 5 0 0 0-5 5c0 3.5 5 9 5 9s5-5.5 5-9a5 5 0 0 0-5-5zm0 7a2 2 0 1 1 0-4 2 2 0 0 1 0 4z"/></svg>address</li>
      </ul>
    </div>
  </section>
</main>
</body>
</html>
```